Video App Design

Test of Compatibility
We are looking for a creative designer who is capable of designing mobile application in a trendy manner and at the same time taking into consideration User Interface and technical logic.
This simple test of the design will include 4 different pages, that fits together. In addition, the functions of each page should include the logical buttons required (example Back Button).
1st Page: Design a Video page for Mobile Application.
(Imaging a App which only showcase video shared on Plumerio)
This includes the size size of the video (4:3 and/or 16:9)
The Video should be able to play directly off the page.
The Video layout should include:
1) User Profile Picture and Name
2) Video Name
3) Like Counter/Button
4) Share Button
5) A 160 Character description
6) 5 additional generic icons
7) Rating (Optional)
The toolbar should include the following functions:
1) Change categories
2) Filter
3) Search
4) A Slider Button
2nd Page: Design a Profile Page
It should include:
1) Profile Picture
2) Edit Profile
3) Number of followers
4) Videos that were uploaded by user
5) A button to show videos shared by the User
6) A button to show videos Like by the User
7) An Icon to show verified Account
8) Upload video (Optional: If not, where should this be)
2nd Page Part II - Edit Profile
This will include the fields to be included
1) Real Name
2) Display Name
3) Email Address and change email
4) Password and change password
5) A 160 Character description of the User. (with character count)
2nd Page Part III: Add Video Page
It should include:
1) Choosing categories and subcategories
2) Upload Pictures (Preview of final picture to be uploaded)
3) Upload Video
4) Video Name (preview of final video to be uploaded)
5) Video Description (with character counter)
6) A Huge chunk of words (Example:Terms and Condition)
3rd Page: A Pop up of Video Page
This would include
1) Video
2) Pictures added to the Video
1) User Profile Picture
2) A button to follow the user
3) Video Name
4) Like Counter/Button
5) Share Button
6) A 160 Character description
7) 5 additional generic icons
8) Video Description
9) Rating (Optional)
10) Reviews
11) Displaying the huge chunk of words (Example:Terms and Condition)
You can contact me at info@tarvenhollow.com for more information.

```html
<!DOCTYPE html>
<html lang="en">
<head>
<meta charset="utf-8">
<title>Video App – Screens</title>
<link href="https://fonts.googleapis.com/css2?family=Ubuntu:wght@400;500;700&display=swap" rel="stylesheet">
<style>
:root{
  --blue:#3b5a9a;
  --blue-dark:#2b4274;
  --navy:#22355f;
  --paper:#ececec;
  --row:#c4c4c4;
  --row-alt:#d8d8d8;
  --white:#ffffff;
  --red:#e23b3b;
  --text-blue:#2b4a8a;
  --bg:#ffffff;
}
*{box-sizing:border-box;margin:0;padding:0}
html,body{width:1200px;height:1000px;overflow:hidden;background:var(--bg);font-family:'Ubuntu',sans-serif}
.canvas{position:relative;width:1200px;height:1000px}
.screen{position:absolute;width:185px;height:328px;overflow:hidden;background:var(--paper)}
.row-top{top:90px}.row-bottom{top:573px}
.col-1{left:82px}.col-2{left:360px}.col-3{left:645px}.col-4{left:922px}
svg.icon{width:10px;height:10px;fill:var(--white)}
.app{position:absolute;top:0;left:0;width:185px;height:328px;background:var(--paper)}
.app.shifted{left:92px}
.topbar{position:absolute;top:0;left:0;right:0;height:22px;background:var(--blue);color:var(--white);display:flex;align-items:center;justify-content:center;font-weight:700;font-size:13px;white-space:nowrap}
.topbar .menu-btn{position:absolute;left:6px;top:6px}
.topbar .avatar-btn{position:absolute;right:4px;top:3px;width:16px;height:16px;border-radius:50%;background:radial-gradient(circle at 50% 40%,#9a9a9a,#3c3c3c);border:1px solid var(--white)}
.feed{position:absolute;top:22px;bottom:30px;left:0;right:0;padding:8px 12px;overflow:hidden}
.card{background:var(--blue);color:var(--white);margin-bottom:10px;border:1px solid var(--blue-dark)}
.card-head{display:flex;justify-content:space-between;align-items:center;height:12px;padding:0 3px;font-size:5.5px;font-weight:700;white-space:nowrap}
.card-user{display:flex;align-items:center;gap:2px}
.mini-avatar{display:inline-block;width:8px;height:8px;border-radius:50%;background:linear-gradient(#c9a27a,#7a5a3c)}
.card-video{height:88px;display:flex;align-items:center;justify-content:center}
.video-crowd{background:linear-gradient(160deg,#5b5550,#2d2a2a 60%,#4a3e36)}
.video-city{background:linear-gradient(180deg,#9a9a98,#6e6c6a 60%,#4c4b4a)}
.video-game{background:linear-gradient(150deg,#3a3f44,#24282c 60%,#4a4d50)}
.video-lake{background:linear-gradient(180deg,#6f97b8,#3c6687 55%,#2d4a63)}
.video-street{background:linear-gradient(170deg,#6b5040,#3a2a22)}
.play{width:24px;height:28px;fill:rgba(255,255,255,.75)}
.card-stats{font-size:4.5px;text-align:center;height:9px;line-height:9px;border-bottom:1px solid rgba(255,255,255,.6);white-space:nowrap}
.card-desc{font-size:5.3px;font-weight:700;line-height:6.5px;padding:2px 3px;height:34px;overflow:hidden}
.card-row{display:flex;justify-content:space-between;align-items:center;font-size:5.5px;font-weight:700;height:12px;padding:0 3px;border-top:1px solid rgba(255,255,255,.6)}
.card-actions{display:flex;height:14px;border-top:1px solid rgba(255,255,255,.6)}
.card-actions span{flex:1;display:flex;align-items:center;justify-content:center;border-right:1px solid rgba(255,255,255,.6)}
.card-actions span:last-child{border-right:none}
.card-actions svg{width:8px;height:8px;fill:var(--white)}
.tabbar{position:absolute;bottom:0;left:0;right:0;height:30px;display:flex;background:var(--blue)}
.tabbar span{flex:1;display:flex;align-items:center;justify-content:center;border-right:2px solid var(--paper)}
.tabbar span:last-child{border-right:none}
.tabbar span.active{background:var(--navy)}
.tabbar svg{width:18px;height:18px;fill:var(--white)}
.drawer{position:absolute;top:0;left:0;width:92px;height:328px;background:var(--blue);color:var(--white);font-size:5.5px;font-weight:700}
.search{margin:5px 4px 6px;height:9px;background:#cfd3da;border-radius:2px;color:var(--text-blue);font-size:5px;display:flex;align-items:center;justify-content:space-between;padding:0 3px}
.search svg{width:6px;height:6px;fill:#6a7690}
.drawer-item{display:flex;justify-content:space-between;align-items:center;height:15px;padding:0 4px;border-top:1px solid rgba(255,255,255,.7)}
.drawer-item:last-of-type{border-bottom:1px solid rgba(255,255,255,.7)}
.drawer-item svg{width:6px;height:6px;fill:var(--white)}
.cat{display:flex;justify-content:space-between;align-items:center;height:15px;padding:0 4px;border-bottom:1px solid var(--white)}
.cat i{width:6px;height:6px;border:1px solid var(--white);border-radius:1px}
.drawer-foot{position:absolute;bottom:6px;left:0;right:0;text-align:center;font-size:4px;font-weight:500}
.profile-top{position:absolute;top:22px;left:0;right:0;height:74px;background:var(--blue);color:var(--white);text-align:center}
.photo{position:relative;width:40px;height:40px;margin:3px auto 2px;border-radius:50%;background:radial-gradient(circle at 50% 45%,#e2e2e2,#8a8a8a);border:2px solid var(--white)}
.verified{position:absolute;right:-3px;top:-1px;width:11px;height:11px}
.p-name{font-size:8px;font-weight:700}
.p-meta{font-size:5px;font-weight:700;margin-top:1px}
.dots{font-size:6px;line-height:6px;opacity:.8}
.tabs{position:absolute;top:96px;left:0;right:0;height:18px;display:flex;border-top:2px solid var(--white)}
.tabs span{flex:1;display:flex;align-items:center;justify-content:center;background:var(--blue);color:var(--white);font-size:7px;font-weight:700;border-right:2px solid var(--white)}
.tabs span:last-child{border-right:none}
.tabs span.active{background:var(--navy)}
.profile-feed{top:122px}
.form{position:absolute;top:90px;left:0;right:0}
.f-row{display:flex;justify-content:space-between;align-items:center;height:15.5px;padding:0 4px;background:var(--row);color:var(--white);font-size:6px;font-weight:700;border-bottom:1px solid #f0f0f0;white-space:nowrap}
.f-row:nth-child(even){background:#b4b4b4}
.f-row b{color:var(--text-blue);font-weight:700}
.f-row svg{width:6px;height:6px;fill:var(--text-blue)}
.f-section{height:15.5px;display:flex;align-items:center;justify-content:center;background:var(--row-alt);color:var(--text-blue);font-size:6px;font-weight:700}
.f-btn{height:15.5px;display:flex;align-items:center;justify-content:center;background:var(--red);color:var(--white);font-size:7px;font-weight:700}
.image-well{height:82px;background:var(--paper);display:flex;align-items:center;justify-content:center}
.image-preview{width:122px;height:70px;background:linear-gradient(160deg,#6c7c5a,#3f4a36 55%,#5a5040)}
.p-action{font-size:5px;font-weight:700;margin-top:1px}
</style>
</head>
<body>
<svg width="0" height="0" style="position:absolute" aria-hidden="true">
  <symbol id="i-menu" viewBox="0 0 10 10"><rect y="1" width="10" height="1.6"/><rect y="4.2" width="10" height="1.6"/><rect y="7.4" width="10" height="1.6"/></symbol>
  <symbol id="i-home" viewBox="0 0 20 20"><path d="M10 2 1 10h3v8h4.5v-5h3v5H16v-8h3z"/></symbol>
  <symbol id="i-user" viewBox="0 0 20 20"><circle cx="10" cy="6" r="4.5"/><path d="M2 19c0-5 3.5-7.5 8-7.5s8 2.5 8 7.5z"/></symbol>
  <symbol id="i-film" viewBox="0 0 20 20"><path d="M1 3h18v14H1zM2.5 4.5v2h2v-2zm0 4.5v2h2V9zm0 4.5v2h2v-2zm13-9v2h2v-2zm0 4.5v2h2V9zm0 4.5v2h2v-2zM8 6.5v7l5.5-3.5z" fill-rule="evenodd"/></symbol>
  <symbol id="i-like" viewBox="0 0 10 10"><path d="M1 4.5h2V9H1zM3.5 4.5 5.5 1c1 0 1.3.8 1 2l-.3 1.2H9c.6 0 .9.5.8 1l-.8 3.3c-.1.3-.4.5-.8.5H3.5z"/></symbol>
  <symbol id="i-share" viewBox="0 0 10 10"><circle cx="8" cy="2" r="1.6"/><circle cx="2" cy="5" r="1.6"/><circle cx="8" cy="8" r="1.6"/><path d="M2 4.6 7.8 1.6l.4.8L2.4 5.4zM2.4 4.6l5.8 3-.4.8L2 5.4z"/></symbol>
  <symbol id="i-comment" viewBox="0 0 10 10"><path d="M1 1.5h8v5.5H5L2.5 9V7H1z"/></symbol>
  <symbol id="i-more" viewBox="0 0 10 10"><circle cx="1.6" cy="5" r="1.3"/><circle cx="5" cy="5" r="1.3"/><circle cx="8.4" cy="5" r="1.3"/></symbol>
  <symbol id="i-play" viewBox="0 0 24 28"><path d="M0 0 24 14 0 28z"/></symbol>
  <symbol id="i-right" viewBox="0 0 10 10"><path d="M3 1 7 5 3 9 2.2 8.2 5.4 5 2.2 1.8z"/></symbol>
  <symbol id="i-down" viewBox="0 0 10 10"><path d="M1 3 5 7 9 3 8.2 2.2 5 5.4 1.8 2.2z"/></symbol>
  <symbol id="i-search" viewBox="0 0 10 10"><path d="M4 0a4 4 0 0 1 3.2 6.4L10 9.2 9.2 10 6.4 7.2A4 4 0 1 1 4 0zm0 1.5a2.5 2.5 0 1 0 0 5 2.5 2.5 0 0 0 0-5z"/></symbol>
  <symbol id="i-tick" viewBox="0 0 12 12"><circle cx="6" cy="6" r="5.5" fill="#2a9df4" stroke="#fff"/><path d="M3.2 6.2 5.2 8 8.8 4" fill="none" stroke="#fff" stroke-width="1.4"/></symbol>
  <symbol id="i-clock" viewBox="0 0 10 10"><path d="M5 0a5 5 0 1 1 0 10A5 5 0 0 1 5 0zm0 1.2a3.8 3.8 0 1 0 0 7.6 3.8 3.8 0 0 0 0-7.6zM4.4 2.5h1.2v2.3l1.8 1.1-.6 1L4.4 5.5z"/></symbol>
  <symbol id="i-star" viewBox="0 0 10 10"><path d="M5 .5 6.3 3.6l3.3.3-2.5 2.2.8 3.3L5 7.6 2.1 9.4l.8-3.3L.4 3.9l3.3-.3z"/></symbol>
  <symbol id="i-plus" viewBox="0 0 10 10"><path d="M5 0a5 5 0 1 1 0 10A5 5 0 0 1 5 0zM4.3 2.5v2h-2v1h2v2h1.4v-2h2v-1h-2v-2z"/></symbol>
  <symbol id="i-pen" viewBox="0 0 10 10"><path d="M7 1 9 3 3.5 8.5 1 9l.5-2.5z"/></symbol>
</svg>

<main class="canvas">

  <!-- Home feed -->
  <section class="screen row-top col-1">
    <div class="app">
      <header class="topbar"><svg class="icon menu-btn"><use href="#i-menu"/></svg>Video App<span class="avatar-btn" role="img" aria-label="User avatar"></span></header>
      <div class="feed">
        <article class="card">
          <header class="card-head"><span>Office Shuffle</span><span class="card-user">Tom Varley <i class="mini-avatar" role="img" aria-label="Tom Varley avatar"></i></span></header>
          <div class="card-video video-crowd" role="img" aria-label="Video still of a crowd dancing"><svg class="play"><use href="#i-play"/></svg></div>
          <p class="card-stats">18,765 Likes • 3,211 Shares • 723 Comments</p>
          <p class="card-desc">Our attempt at the Office Shuffle. Let us know what you guys think!!</p>
          <nav class="card-actions"><span><svg><use href="#i-like"/></svg></span><span><svg><use href="#i-share"/></svg></span><span><svg><use href="#i-comment"/></svg></span><span><svg><use href="#i-more"/></svg></span></nav>
        </article>
        <article class="card">
          <header class="card-head"><span>Winter Wonderland (Moscow)</span><span class="card-user">Lena Marsh <i class="mini-avatar" role="img" aria-label="Lena Marsh avatar"></i></span></header>
          <div class="card-video video-city" role="img" aria-label="Video still of a snowy city square"><svg class="play"><use href="#i-play"/></svg></div>
        </article>
      </div>
      <nav class="tabbar"><span class="active"><svg><use href="#i-home"/></svg></span><span><svg><use href="#i-user"/></svg></span><span><svg><use href="#i-film"/></svg></span></nav>
    </div>
  </section>

  <!-- Drawer -->
  <section class="screen row-top col-2">
    <aside class="drawer">
      <div class="search">Search<svg><use href="#i-search"/></svg></div>
      <div class="drawer-item">Change Category<svg><use href="#i-right"/></svg></div>
      <div class="drawer-item">Filter<svg><use href="#i-right"/></svg></div>
      <p class="drawer-foot">2014. All Rights Reserved. VIDEO APP.</p>
    </aside>
    <div class="app shifted">
      <header class="topbar"><svg class="icon menu-btn"><use href="#i-menu"/></svg>Video App<span class="avatar-btn" role="img" aria-label="User avatar"></span></header>
      <div class="feed">
        <article class="card">
          <header class="card-head"><span>Office Shuffle</span><span class="card-user">Tom Varley <i class="mini-avatar" role="img" aria-label="Tom Varley avatar"></i></span></header>
          <div class="card-video video-crowd" role="img" aria-label="Video still of a crowd dancing"><svg class="play"><use href="#i-play"/></svg></div>
          <p class="card-stats">18,765 Likes • 3,211 Shares • 723 Comments</p>
          <p class="card-desc">Our attempt at the Office Shuffle. Let us know what you guys think!!</p>
          <nav class="card-actions"><span><svg><use href="#i-like"/></svg></span><span><svg><use href="#i-share"/></svg></span><span><svg><use href="#i-comment"/></svg></span><span><svg><use href="#i-more"/></svg></span></nav>
        </article>
        <article class="card">
          <header class="card-head"><span>Winter Wonderland (Moscow)</span><span class="card-user">Lena Marsh</span></header>
          <div class="card-video video-city" role="img" aria-label="Video still of a snowy city square"><svg class="play"><use href="#i-play"/></svg></div>
        </article>
      </div>
      <nav class="tabbar"><span class="active"><svg><use href="#i-home"/></svg></span><span><svg><use href="#i-user"/></svg></span><span><svg><use href="#i-film"/></svg></span></nav>
    </div>
  </section>

  <!-- Drawer: categories -->
  <section class="screen row-top col-3">
    <aside class="drawer">
      <div class="search">Search<svg><use href="#i-search"/></svg></div>
      <div class="drawer-item">Change Category<svg><use href="#i-down"/></svg></div>
      <div class="cat" style="background:#ff8c00">Animals<i></i></div>
      <div class="cat" style="background:#1e90ff">Cars<i></i></div>
      <div class="cat" style="background:#22dd88">Comedy<i></i></div>
      <div class="cat" style="background:#d63bea">Dance<i></i></div>
      <div class="cat" style="background:#f0a030">Food<i></i></div>
      <div class="cat" style="background:#a0584a">Gaming<i></i></div>
      <div class="cat" style="background:#1f3a6e">Music<i></i></div>
      <div class="cat" style="background:#e0262a">Technology<i></i></div>
      <div class="cat" style="background:#3fcf2a">Sport<i></i></div>
      <div class="drawer-item">Filter<svg><use href="#i-right"/></svg></div>
      <p class="drawer-foot">2014. All Rights Reserved. VIDEO APP.</p>
    </aside>
    <div class="app shifted">
      <header class="topbar"><svg class="icon menu-btn"><use href="#i-menu"/></svg>Video App</header>
      <div class="feed">
        <article class="card">
          <header class="card-head"><span>Office Shuffle</span><span class="card-user">Tom Varley</span></header>
          <div class="card-video video-crowd" role="img" aria-label="Video still of a crowd dancing"><svg class="play"><use href="#i-play"/></svg></div>
          <p class="card-stats">18,765 Likes • 3,211 Shares • 723 Comments</p>
          <p class="card-desc">Our attempt at the Office Shuffle. Let us know what you guys think!!</p>
          <nav class="card-actions"><span><svg><use href="#i-like"/></svg></span><span><svg><use href="#i-share"/></svg></span><span><svg><use href="#i-comment"/></svg></span><span><svg><use href="#i-more"/></svg></span></nav>
        </article>
        <article class="card">
          <header class="card-head"><span>Winter Wonderland (Moscow)</span><span class="card-user">Lena Marsh</span></header>
          <div class="card-video video-city" role="img" aria-label="Video still of a snowy city square"><svg class="play"><use href="#i-play"/></svg></div>
        </article>
      </div>
      <nav class="tabbar"><span class="active"><svg><use href="#i-home"/></svg></span><span><svg><use href="#i-user"/></svg></span><span><svg><use href="#i-film"/></svg></span></nav>
    </div>
  </section>

  <!-- Drawer: filter -->
  <section class="screen row-top col-4">
    <aside class="drawer">
      <div class="search">Search<svg><use href="#i-search"/></svg></div>
      <div class="drawer-item">Change Category<svg><use href="#i-right"/></svg></div>
      <div class="drawer-item">Filter<svg><use href="#i-down"/></svg></div>
      <div class="drawer-item">Most Popular<svg><use href="#i-like"/></svg></div>
      <div class="drawer-item">Most Recent<svg><use href="#i-clock"/></svg></div>
      <div class="drawer-item">Your Favourites<svg><use href="#i-star"/></svg></div>
      <p class="drawer-foot">2014. All Rights Reserved. VIDEO APP.</p>
    </aside>
    <div class="app shifted">
      <header class="topbar"><svg class="icon menu-btn"><use href="#i-menu"/></svg>Video App</header>
      <div class="feed">
        <article class="card">
          <header class="card-head"><span>Office Shuffle</span><span class="card-user">Tom Varley</span></header>
          <div class="card-video video-crowd" role="img" aria-label="Video still of a crowd dancing"><svg class="play"><use href="#i-play"/></svg></div>
          <p class="card-stats">18,765 Likes • 3,211 Shares • 723 Comments</p>
          <p class="card-desc">Our attempt at the Office Shuffle. Let us know what you guys think!!</p>
          <nav class="card-actions"><span><svg><use href="#i-like"/></svg></span><span><svg><use href="#i-share"/></svg></span><span><svg><use href="#i-comment"/></svg></span><span><svg><use href="#i-more"/></svg></span></nav>
        </article>
        <article class="card">
          <header class="card-head"><span>Winter Wonderland (Moscow)</span><span class="card-user">Lena Marsh</span></header>
          <div class="card-video video-city" role="img" aria-label="Video still of a snowy city square"><svg class="play"><use href="#i-play"/></svg></div>
        </article>
      </div>
      <nav class="tabbar"><span class="active"><svg><use href="#i-home"/></svg></span><span><svg><use href="#i-user"/></svg></span><span><svg><use href="#i-film"/></svg></span></nav>
    </div>
  </section>

  <!-- Profile -->
  <section class="screen row-bottom col-1">
    <header class="topbar"><svg class="icon menu-btn"><use href="#i-menu"/></svg>Profile</header>
    <div class="profile-top">
      <div class="photo" role="img" aria-label="Profile photo of Aled Corwin"><svg class="verified"><use href="#i-tick"/></svg></div>
      <p class="p-name">Aled Corwin</p>
      <p class="p-meta">7,332 Followers | 243 Following</p>
      <p class="dots">• •</p>
    </div>
    <nav class="tabs"><span class="active">Uploads</span><span>Likes</span><span>Shares</span></nav>
    <div class="feed profile-feed">
      <article class="card">
        <header class="card-head"><span>Let's Play: AVF!</span><span class="card-user">Aled Corwin <i class="mini-avatar" role="img" aria-label="Aled Corwin avatar"></i></span></header>
        <div class="card-video video-game" role="img" aria-label="Video still from a war shooter game"><svg class="play"><use href="#i-play"/></svg></div>
        <p class="card-stats">4,619 Likes • 933 Shares • 201 Comments</p>
        <p class="card-desc">Me playing the new Ashfall Protocol: Vanta Front! So far, so good! Definitely gonna be playing this a lot! What are your guys thoughts?</p>
        <nav class="card-actions"><span><svg><use href="#i-like"/></svg></span><span><svg><use href="#i-share"/></svg></span><span><svg><use href="#i-comment"/></svg></span><span><svg><use href="#i-more"/></svg></span></nav>
      </article>
    </div>
    <nav class="tabbar"><span><svg><use href="#i-home"/></svg></span><span class="active"><svg><use href="#i-user"/></svg></span><span><svg><use href="#i-film"/></svg></span></nav>
  </section>

  <!-- Edit profile -->
  <section class="screen row-bottom col-2">
    <header class="topbar"><svg class="icon menu-btn"><use href="#i-menu"/></svg>Profile</header>
    <div class="profile-top">
      <div class="photo" role="img" aria-label="Profile photo of Aled Corwin"><svg class="verified"><use href="#i-tick"/></svg></div>
      <p class="p-name">Aled Corwin</p>
      <p class="p-action">Edit Profile <svg class="icon" style="width:5px;height:5px"><use href="#i-pen"/></svg></p>
    </div>
    <div class="form">
      <div class="f-section">Profile</div>
      <div class="f-row">Name<b>Aled Corwin</b></div>
      <div class="f-row">Display Name<b>Aled Corwin</b></div>
      <div class="f-row">Profile Image<svg><use href="#i-right"/></svg></div>
      <div class="f-row">Profile Description<b>Hi. I'm Aled! I up...</b></div>
      <div class="f-section">Account</div>
      <div class="f-row">Email<b>aledcorwin3@postly.net</b></div>
      <div class="f-row">Change Email<svg><use href="#i-right"/></svg></div>
      <div class="f-row">Password<b>A*******</b></div>
      <div class="f-row">Change Password<svg><use href="#i-right"/></svg></div>
      <div class="f-row">Notifications<svg><use href="#i-right"/></svg></div>
      <div class="f-row">Privacy<svg><use href="#i-right"/></svg></div>
      <div class="f-btn">Log Out</div>
    </div>
    <nav class="tabbar"><span><svg><use href="#i-home"/></svg></span><span class="active"><svg><use href="#i-user"/></svg></span><span><svg><use href="#i-film"/></svg></span></nav>
  </section>

  <!-- Upload video -->
  <section class="screen row-bottom col-3">
    <header class="topbar"><svg class="icon menu-btn"><use href="#i-menu"/></svg>Profile</header>
    <div class="profile-top">
      <div class="photo" role="img" aria-label="Profile photo of Aled Corwin"><svg class="verified"><use href="#i-tick"/></svg></div>
      <p class="p-name">Aled Corwin</p>
      <p class="p-action">Upload Video <svg class="icon" style="width:5px;height:5px"><use href="#i-plus"/></svg></p>
    </div>
    <div class="form">
      <div class="f-row">Video Name<b>Let's Play: Tilemoor!</b></div>
      <div class="f-row">Category<b>Gaming</b></div>
      <div class="f-row">Video Description<b>Watch me play so...</b></div>
      <div class="f-row">Video Image<svg><use href="#i-down"/></svg></div>
      <div class="image-well"><div class="image-preview" role="img" aria-label="Thumbnail preview of a blocky game scene"></div></div>
      <div class="f-row">Terms &amp; Conditions<b>All rights reser...</b></div>
      <div class="f-row">Privacy<svg><use href="#i-right"/></svg></div>
      <div class="f-row">Preview<svg><use href="#i-right"/></svg></div>
      <div class="f-btn">Upload Video</div>
    </div>
    <nav class="tabbar"><span><svg><use href="#i-home"/></svg></span><span class="active"><svg><use href="#i-user"/></svg></span><span><svg><use href="#i-film"/></svg></span></nav>
  </section>

  <!-- Videos -->
  <section class="screen row-bottom col-4">
    <header class="topbar"><svg class="icon menu-btn"><use href="#i-menu"/></svg>Videos<span class="avatar-btn" role="img" aria-label="User avatar"></span></header>
    <div class="feed">
      <article class="card">
        <header class="card-head"><span>Humans Are Amazing 2014</span><span class="card-user">Jo Pennick <i class="mini-avatar" role="img" aria-label="Jo Pennick avatar"></i></span></header>
        <div class="card-video video-lake" role="img" aria-label="Video still of a person leaping into a lake"><svg class="play"><use href="#i-play"/></svg></div>
        <p class="card-stats">43,907 Likes • 10,012 Shares • 3492 Comments</p>
        <p class="card-desc">Videos from all over the internet gathered together, to create a montage of people doing extraordinary things in 2014! Enjoy and please share!</p>
        <div class="card-row">Reviews (23)<svg class="icon" style="width:6px;height:6px"><use href="#i-right"/></svg></div>
        <nav class="card-actions"><span><svg><use href="#i-like"/></svg></span><span><svg><use href="#i-share"/></svg></span><span><svg><use href="#i-comment"/></svg></span><span><svg><use href="#i-more"/></svg></span></nav>
      </article>
      <article class="card">
        <header class="card-head"><span>The Ferry Road Shouter</span><span class="card-user">Sam Rudd <i class="mini-avatar" role="img" aria-label="Sam Rudd avatar"></i></span></header>
        <div class="card-video video-street" role="img" aria-label="Video still of a man on a street"><svg class="play"><use href="#i-play"/></svg></div>
      </article>
    </div>
    <nav class="tabbar"><span><svg><use href="#i-home"/></svg></span><span><svg><use href="#i-user"/></svg></span><span class="active"><svg><use href="#i-film"/></svg></span></nav>
  </section>

</main>
</body>
</html>
```